Modern and innovative greeting cards for an internal electronic manufacturing services company

Corvanetix is an international electronic manufacturing services (EMS) company. It Operates 18 manufacturing locations on four continents with a headcount of around 5,200 employed. The company Was founded in Paris, France in 1999 and offers comprehensive and integrated design and manufacturing services from initial product design to volume manufacture Including prototyping, direct order fulfillment and post deployment services. Corvanetix Thrives ict single positioning on the market: - Local shares with teams of experts in Each of ict rentals Offering local services and strong customer focus, along with Harmonized equipment and processes in the factories Facilitating transfers. - Global mindset, with a worldwide footprint Strengthened by purchasing capabilities and supply chain organization on 4 continents. Visit our Website for more details: www.corvanetix-demo.net. Today we need a professional design for our 2017 Greeting cards, with The Following characteristics: - These cards will be in 7 different languages ​​(We provide the text). - Digital (to be sent by email we publish Social Network / .jpeg preferably format), aim with the possibility to print Them - Look & Feel: highly technological, high tech, innovation, electronic / partnership / shaping the future ... - Main colors to be used: o Blue (R = 36 / L = 84 / B = 157) o Red (R = 189 / G = 13 / B = 46) o Grey (R = 115 / G = 114 / B = 114) - Others colors can be added to create modernity and surprise. - Originality is expected Regarding the design. More comments Will Be Given the first ounce Proposals are received. You will find attached: example of our 2014 greeting cards translation in the 7 languages. To select the design, a version in just one language is ok (English). Once the design of the greeting card is selected, the designer will Provide the six other versions with different text. Thank you in advance. Kind regards, Lorraine K

Target Market(s)

All Corvanetix customers. Corvanetix is a subcontractor and can work with customers from different markets Many: automotive, industrial, energy, data processing, medical, defense & Aerospace.

Industry/Entity Type

Electronics

Requirements
Must have
• Look and feel: electronics / modern / technology / High tech / Professional / Sobriety. Respect of the color code as MENTIONED Above in the description (blue / gray / red with numeric Their respective colors (RGB)). . Corvanetix Logo (See attachment). 7 different versions for the 7 Provided languages. Digital format allows printing That release.
Nice to have
• Additional colors Appearance of Printed Circuit Board somewhere
Should not have
• Any "bucolic" reference or too much color or too many "information"

```html
<!DOCTYPE html>
<html lang="en">
<head>
<meta charset="utf-8">
<title>Corvanetix 2017 Greeting Card</title>
<link rel="stylesheet" href="https://fonts.googleapis.com/css2?family=Montserrat:wght@600;700&family=Source+Sans+3:wght@400;600&display=swap">
<style>
  :root {
    --page-bg: #e8e9eb;
    --card-white: #ffffff;
    --brand-blue: #24549d;
    --brand-red: #bd0d2e;
    --brand-grey: #737272;
    --headline-blue: #1a4a9c;
    --strip-light: #c8d3ea;
    --band-deep: #0e3f8e;
    --band-mid: #0b5aa2;
  }
  * { margin: 0; padding: 0; box-sizing: border-box; }
  html, body {
    width: 1200px;
    height: 673px;
    overflow: hidden;
    background: var(--page-bg);
  }
  .greeting-card {
    position: absolute;
    left: 126px;
    top: 86px;
    width: 940px;
    height: 474px;
    background: var(--card-white);
    overflow: hidden;
  }
  .card-header {
    position: relative;
    height: 120px;
  }
  .brand {
    position: absolute;
    left: 42px;
    top: 38px;
  }
  .brand-name {
    display: flex;
    align-items: center;
    gap: 10px;
    font-family: "Montserrat", sans-serif;
    font-weight: 700;
    font-size: 24px;
    letter-spacing: 0.5px;
    color: var(--brand-grey);
    line-height: 1;
  }
  .brand-mark {
    width: 22px;
    height: 22px;
    background: var(--brand-red);
  }
  .brand-tagline {
    margin-top: 9px;
    margin-left: 32px;
    font-family: "Source Sans 3", sans-serif;
    font-size: 11px;
    letter-spacing: 6px;
    color: var(--brand-grey);
  }
  .headline {
    position: absolute;
    right: 27px;
    top: 63px;
    font-family: "Source Sans 3", sans-serif;
    font-size: 21px;
    color: var(--headline-blue);
    white-space: nowrap;
  }
  .hero {
    position: relative;
    height: 258px;
    margin-left: 2px;
  }
  .hero-visual {
    position: absolute;
    inset: 0;
    background:
      radial-gradient(ellipse at 62% 55%, rgba(255,240,230,0.85) 0%, rgba(255,220,225,0.3) 18%, transparent 40%),
      linear-gradient(90deg, #3e6fa8 0%, #5d8fc0 22%, #7aa8cc 38%, #b9a7c6 58%, #d3b3c6 75%, #b2a3c2 100%);
  }
  .hero-year {
    position: absolute;
    right: 26px;
    top: 30px;
    font-family: "Montserrat", sans-serif;
    font-weight: 600;
    font-size: 218px;
    line-height: 1;
    letter-spacing: -4px;
    color: rgba(255,255,255,0.82);
  }
  .light-strip {
    height: 17px;
    background: var(--strip-light);
  }
  .footer-band {
    height: 79px;
    background: linear-gradient(90deg, var(--band-deep), var(--band-mid));
  }
</style>
</head>
<body>
  <main class="greeting-card">
    <header class="card-header">
      <div class="brand">
        <div class="brand-name"><span class="brand-mark"></span>CORVANETIX</div>
        <div class="brand-tagline">YOUR EMS PARTNER</div>
      </div>
      <p class="headline">The entire Corvanetix team wishes you great success for</p>
    </header>
    <section class="hero">
      <div class="hero-visual" role="img" aria-label="Dome of tiled electronics imagery — circuit boards, chips and schematics — fading into a soft pink glow"></div>
      <div class="hero-year">2017</div>
    </section>
    <div class="light-strip"></div>
    <div class="footer-band"></div>
  </main>
</body>
</html>
```